Harbor Nightclub

Nightclub flyer., digital single sided, for KV and PX. I included samples of some previous flyers we've used. Sample Info:
HARBOR
FRIDAYS
FRI MAY 1 2020
DJ VORTAN (club floor)
DJ RUZO & DJ TAV (residents on the lounge floor)
4217 Marlow Avenue Sacramento
www.harborvenuehall.example for list/VIP inquiries

Target Market(s)

Upscale top 40 crowd but want some cool and artsy like the examples included.

Font styles to use
Sans Serif

Requirements
Must have
• Harbor Logo
Nice to have
• Would be nice if the flyer can be incorporated later with DJ photos (sometimes we will add dj photos to pixagram etc). Would like a big city type of feel.
Should not have
• Nothing too sexual.

```html
<!DOCTYPE html>
<html lang="en">
<head>
<meta charset="utf-8">
<title>Harbor Fridays — Flyer</title>
<link rel="stylesheet" href="https://fonts.googleapis.com/css2?family=Open+Sans:wght@400;600&display=swap">
<style>
  :root {
    --bg-plum: #231820;
    --bg-navy: #1b1a2f;
    --ink: #ffffff;
    --accent-yellow: #c9c233;
    --ring-violet: #4a47c8;
    --ring-dusk: #6a4a86;
    --photo-light: #9b9499;
    --photo-dark: #8c8e96;
  }
  * { margin: 0; padding: 0; box-sizing: border-box; }
  html, body { width: 844px; height: 1200px; overflow: hidden; background: var(--bg-plum); }
  body { font-family: "Open Sans", sans-serif; color: var(--ink); }

  .flyer {
    position: relative;
    width: 844px;
    height: 1200px;
    overflow: hidden;
    background: linear-gradient(115deg, var(--bg-plum) 0%, var(--bg-plum) 45%, var(--bg-navy) 100%);
  }

  .backdrop-art { position: absolute; left: 0; top: 0; width: 844px; height: 1200px; }

  .title-line { position: absolute; font-weight: 400; line-height: 1; text-transform: uppercase; white-space: nowrap; }
  .title-venue {
    left: 80px; top: 116px; font-size: 53px; letter-spacing: 24px;
    display: flex; align-items: flex-end;
  }
  .title-rule {
    display: inline-block; width: 122px; height: 4px; margin-bottom: 8px;
    background: var(--ink); letter-spacing: 0;
  }
  .title-night { left: 305px; top: 187px; font-size: 53px; letter-spacing: 19px; }

  .vertical { position: absolute; writing-mode: vertical-rl; transform: rotate(180deg); white-space: nowrap; }
  .event-date { left: 78px; top: 380px; font-size: 29px; letter-spacing: 12px; line-height: 1; }
  .event-web { left: 117px; top: 291px; font-size: 12px; letter-spacing: 1.8px; color: var(--accent-yellow); line-height: 1; }

  .floor-label { position: absolute; font-size: 11.5px; letter-spacing: 1.6px; text-transform: uppercase; }
  .floor-club { left: 479px; top: 670px; }
  .floor-lounge { left: 471px; top: 912px; }

  .dj-photo {
    position: absolute; width: 142px; height: 142px; border-radius: 50%;
    background: linear-gradient(135deg, var(--photo-light), var(--photo-dark));
  }
  .photo-headliner { left: 471px; top: 697px; }
  .photo-resident-one { left: 471px; top: 952px; }
  .photo-resident-two { left: 660px; top: 950px; }

  .dj-name { position: absolute; font-weight: 600; font-size: 22px; letter-spacing: 3.2px; white-space: nowrap; line-height: 1; }
  .name-headliner { left: 629px; top: 754px; }
  .name-resident-one { left: 483px; top: 1106px; }
  .name-resident-two { left: 693px; top: 1105px; }

  .venue-mark { position: absolute; left: 82px; top: 925px; width: 160px; text-align: center; }
  .venue-mark .mark-ring {
    display: block; width: 70px; height: 70px; margin: 0 auto 12px;
    border: 6px solid var(--ink); border-radius: 50%;
  }
  .venue-mark .mark-name { display: block; font-size: 33px; font-weight: 400; letter-spacing: 1px; line-height: 1; }
  .venue-mark .mark-sub { display: block; margin-top: 6px; font-size: 7.5px; letter-spacing: 1.6px; }

  .venue-address { position: absolute; left: 87px; top: 1087px; font-size: 14px; font-weight: 600; letter-spacing: 2px; line-height: 27px; font-style: normal; }
</style>
</head>
<body>
  <main class="flyer">
    <svg class="backdrop-art" viewBox="0 0 844 1200" role="img" aria-label="Abstract artwork of overlapping concentric vinyl-like rings in violet and dusk purple">
      <defs>
        <radialGradient id="glow-violet" cx="0.5" cy="0.5" r="0.5">
          <stop offset="0" stop-color="#4a47c8" stop-opacity="0.05"/>
          <stop offset="0.75" stop-color="#4a47c8" stop-opacity="0.28"/>
          <stop offset="1" stop-color="#4a47c8" stop-opacity="0"/>
        </radialGradient>
        <radialGradient id="glow-dusk" cx="0.5" cy="0.5" r="0.5">
          <stop offset="0" stop-color="#6a4a86" stop-opacity="0.05"/>
          <stop offset="0.8" stop-color="#6a4a86" stop-opacity="0.22"/>
          <stop offset="1" stop-color="#6a4a86" stop-opacity="0"/>
        </radialGradient>
      </defs>
      <circle cx="500" cy="80" r="340" fill="url(#glow-dusk)"/>
      <circle cx="460" cy="440" r="290" fill="url(#glow-dusk)"/>
      <circle cx="585" cy="495" r="250" fill="url(#glow-violet)"/>
      <circle cx="900" cy="380" r="300" fill="url(#glow-violet)"/>
      <circle cx="820" cy="0" r="120" fill="url(#glow-violet)"/>
    </svg>

    <h1>
      <span class="title-line title-venue">Harbor<span class="title-rule"></span></span>
      <span class="title-line title-night">Fridays</span>
    </h1>

    <p class="vertical event-date">MAY 1 2020</p>
    <p class="vertical event-web">www.harborvenuehall.example for List/VIP inquiries</p>

    <p class="floor-label floor-club">Club Floor</p>
    <div class="dj-photo photo-headliner" role="img" aria-label="Photo of DJ Vortan"></div>
    <p class="dj-name name-headliner">DJ VORTAN</p>

    <p class="floor-label floor-lounge">Residents on the Lounge Floor</p>
    <div class="dj-photo photo-resident-one" role="img" aria-label="Photo of DJ Ruzo"></div>
    <div class="dj-photo photo-resident-two" role="img" aria-label="Photo of DJ Tav"></div>
    <p class="dj-name name-resident-one">DJ&nbsp; RUZO</p>
    <p class="dj-name name-resident-two">DJ TAV</p>

    <div class="venue-mark">
      <span class="mark-ring"></span>
      <span class="mark-name">HARBOR</span>
      <span class="mark-sub">NIGHTCLUB + LOUNGE</span>
    </div>

    <address class="venue-address">
      4217 MARLOW AVENUE<br>SACRAMENTO.
    </address>
  </main>
</body>
</html>
```